Business Card / Appointment Card for Physician

On one side it should give the logo, address, and contact information, and on the other side it should br an Appointment card.

One Side:
Logo (see attached files)
Board Certified American Orthopedic Surgery

1487 Harrowgate Ave.
Suite KM7
Bronx, NY 10527
Tel: (718) 552 - 1948
Fax: (718) 552 - 7210

628 Fourth Ave.
Suite 42
New York, NY 10087
Tel: (212) 734 - 2815

Second Side:
Appointment
give them a choice of Bronx or Mahattan office
For:
Date:
Time:

If you are unable to keep your appointment, please call (718) 263-5102 24hrs in advance.

Target Market(s)

People that need orthopedic surgery

Industry/Entity Type

Business

Contact Information for Business Card

smart and attractive

Requirements
Must have
• logo
• contact information on one side, appointment information on the other

```html
<!DOCTYPE html>
<html lang="en">
<head>
<meta charset="utf-8">
<title>Orthopedic Surgery – Business &amp; Appointment Card</title>
<link rel="stylesheet" href="https://fonts.googleapis.com/css2?family=Arimo:wght@400;700&display=swap">
<style>
  :root {
    --page-bg: #e9e9e6;
    --card-white: #ffffff;
    --brand-green: #7cc242;
    --brand-blue: #0b5fa5;
    --ink: #111111;
    --field-line: #2f6fb3;
    --card-shadow: rgba(0, 0, 0, 0.18);
  }
  * { box-sizing: border-box; margin: 0; padding: 0; }
  html, body {
    width: 1200px; height: 800px; overflow: hidden;
    background: var(--page-bg);
    font-family: "Arimo", Arial, sans-serif;
  }
  .sheet {
    width: 1200px; height: 800px;
    display: flex; flex-direction: column;
    align-items: center; justify-content: center; gap: 30px;
  }
  .card {
    position: relative;
    width: 620px; height: 354px;
    background: var(--card-white);
    box-shadow: 0 6px 18px var(--card-shadow);
    overflow: hidden;
  }
  .card__waves { position: absolute; inset: 0; width: 100%; height: 100%; }

  /* Contact side */
  .contact__title {
    position: absolute; left: 20px; right: 20px; top: 104px;
    text-align: center;
    color: var(--brand-green);
    font-weight: 700; font-size: 19px; letter-spacing: 0.4px;
    text-transform: uppercase;
  }
  .contact__offices {
    position: absolute; left: 70px; right: 70px; top: 150px;
    display: flex; justify-content: space-between;
  }
  .office { color: var(--ink); font-size: 14px; line-height: 1.45; font-style: normal; }
  .office__name { color: var(--brand-blue); font-weight: 700; font-size: 13px; letter-spacing: 0.6px; text-transform: uppercase; margin-bottom: 2px; }

  /* Appointment side */
  .appt__title {
    position: absolute; left: 0; right: 0; top: 60px;
    text-align: center; color: var(--brand-green);
    font-weight: 700; font-size: 26px; letter-spacing: 0.8px;
  }
  .appt__choice {
    position: absolute; left: 0; right: 0; top: 98px;
    text-align: center; color: var(--ink);
    font-weight: 700; font-size: 13.5px; letter-spacing: 0.3px;
  }
  .appt__fields {
    position: absolute; left: 150px; width: 330px; top: 126px;
    display: flex; flex-direction: column; gap: 9px;
  }
  .field {
    height: 30px; border: 1.5px solid var(--field-line);
    background: var(--card-white);
    display: flex; align-items: center; justify-content: center;
    color: var(--brand-green); font-weight: 700; font-size: 16px;
  }
  .appt__note {
    position: absolute; left: 110px; right: 10px; top: 254px;
    text-align: center; color: var(--ink); font-size: 11.5px;
    white-space: nowrap;
  }
</style>
</head>
<body>
<main class="sheet">

  <section class="card card--contact" aria-label="Contact side">
    <svg class="card__waves" viewBox="0 0 620 354" preserveAspectRatio="none" aria-hidden="true">
      <path d="M0 0 H620 V22 C420 30 250 48 0 84 Z" fill="var(--brand-green)"/>
      <path d="M0 72 C240 40 420 22 620 14" fill="none" stroke="#fff" stroke-width="3"/>
      <path d="M0 354 H620 V296 C470 306 320 330 200 354 Z" fill="var(--brand-blue)"/>
      <path d="M236 354 C340 332 480 316 620 310" fill="none" stroke="#fff" stroke-width="3"/>
    </svg>
    <h1 class="contact__title">Board Certified American Orthopedic Surgery</h1>
    <div class="contact__offices">
      <address class="office">
        <div class="office__name">Bronx</div>
        1487 Harrowgate Ave.<br>
        Suite KM7<br>
        Bronx, NY 10527<br>
        Tel: (718) 552 - 1948<br>
        Fax: (718) 552 - 7210
      </address>
      <address class="office">
        <div class="office__name">Manhattan</div>
        628 Fourth Ave.<br>
        Suite 42<br>
        New York, NY 10087<br>
        Tel: (212) 734 - 2815
      </address>
    </div>
  </section>

  <section class="card card--appointment" aria-label="Appointment side">
    <svg class="card__waves" viewBox="0 0 620 354" preserveAspectRatio="none" aria-hidden="true">
      <path d="M0 0 H620 V180 C590 175 560 150 530 110 C490 60 440 30 380 18 C250 -2 100 4 0 10 Z" fill="var(--brand-green)"/>
      <path d="M0 22 C100 16 250 12 380 32 C440 44 490 74 525 122 C555 164 585 188 620 192" fill="none" stroke="#fff" stroke-width="3"/>
      <path d="M0 200 C40 230 70 270 140 300 C260 345 450 346 620 348 V354 H0 Z" fill="var(--brand-blue)"/>
      <path d="M0 186 C44 218 76 258 146 288 C264 332 450 336 620 338" fill="none" stroke="#fff" stroke-width="3"/>
    </svg>
    <h2 class="appt__title">APPOINTMENT</h2>
    <p class="appt__choice">GIVE THEM A CHOICE OF BRONX OR MAHATTAN OFFICE</p>
    <div class="appt__fields">
      <div class="field">FOR:</div>
      <div class="field">DATE:</div>
      <div class="field">TIME:</div>
    </div>
    <p class="appt__note">If you are unable to keep your appointment, please call (718) 263-5102 24hrs in advance.</p>
  </section>

</main>
</body>
</html>
```